Square graphic for social media post

I want to create a 1080 x 1080px all-black image for the quote below that I can share on social media. I want the emphasis to be primarily on the quote, secondarily on the portrait, and third (smallest) on the logo. I want the background on the portrait to be edited so it's transparent and just shows the face of the person on a black background (no brick wall visible).

Graphic color: black
Text color: white
Content: "What we went through is going to make the greatest generation of hoteliers our industry has ever seen." << biggest text
Dorian Welk << smaller text
President, Marrowgate Hotels << smaller text
[image of person - use whichever version looks better to you]
[Add Lodging Ledger logo - whichever looks better to you]

This image needs to be readable when sized down much smaller (400x400?) so want the text and portrait to take up most of the space.

I'd like the output both as PNG and original file (preferably Canva). Thanks!

Target Market(s)

Hotel managers

Industry/Entity Type

Hospitality

Font styles to use
Sans Serif

Colors

Designer to choose colors to be used in the design.

Requirements
Must have
• Needs to focus on the quote and the person quoted (the portrait)

```html
<!DOCTYPE html>
<html lang="en">
<head>
<meta charset="utf-8">
<title>Lodging Ledger – Quote Post</title>
<link href="https://fonts.googleapis.com/css2?family=Libre+Baskerville:wght@400;700&display=swap" rel="stylesheet">
<style>
  :root {
    --page-bg: #17181a;
    --post-bg: #060607;
    --ink: #ffffff;
    --ink-soft: #e8e8e8;
    --rule: #8a8a8a;
    --deco-top: #141416;
    --deco-bottom: rgba(20, 20, 22, 0);
    --portrait-a: #d9d9d9;
    --portrait-b: #2c4a8c;
  }
  * { margin: 0; padding: 0; box-sizing: border-box; }
  html, body {
    width: 675px;
    height: 1200px;
    overflow: hidden;
    background: var(--page-bg);
  }
  body {
    display: flex;
    align-items: center;
    justify-content: center;
    font-family: "Libre Baskerville", Georgia, serif;
    color: var(--ink);
  }
  .quote-post {
    position: relative;
    width: 560px;
    height: 560px;
    background: var(--post-bg);
    overflow: hidden;
  }
  .side-ornament {
    position: absolute;
    top: 0;
    width: 88px;
    height: 294px;
    background: linear-gradient(180deg, var(--deco-top) 0%, var(--deco-top) 70%, var(--deco-bottom) 100%);
  }
  .side-ornament--left { left: 0; border-radius: 0 0 40px 0; }
  .side-ornament--right { right: 0; border-radius: 0 0 0 40px; }

  .brand {
    position: absolute;
    top: 62px;
    left: 0;
    right: 0;
    display: flex;
    align-items: center;
    justify-content: center;
    gap: 8px;
    font-size: 11px;
    font-weight: 700;
    letter-spacing: 3px;
    text-transform: uppercase;
    color: var(--ink);
  }
  .brand__dot {
    width: 7px;
    height: 7px;
    border-radius: 50%;
    background: var(--ink);
  }

  .portrait {
    position: absolute;
    top: 168px;
    left: 50%;
    width: 148px;
    height: 148px;
    margin-left: -74px;
    border-radius: 50%;
    border: 1px solid var(--rule);
    padding: 3px;
  }
  .portrait__photo {
    width: 100%;
    height: 100%;
    border-radius: 50%;
    background: linear-gradient(180deg, var(--portrait-a) 0%, #c9a58c 45%, var(--portrait-b) 100%);
  }

  .quote {
    position: absolute;
    top: 336px;
    left: 0;
    right: 0;
    text-align: center;
    font-size: 20px;
    font-weight: 700;
    line-height: 32px;
    color: var(--ink);
  }
  .quote__rule {
    position: absolute;
    top: 448px;
    left: 50%;
    width: 238px;
    margin-left: -119px;
    height: 1px;
    background: var(--rule);
  }
  .attribution {
    position: absolute;
    top: 458px;
    left: 0;
    right: 0;
    text-align: center;
    font-size: 16px;
    line-height: 24px;
    color: var(--ink-soft);
  }
  .attribution__name { font-weight: 700; color: var(--ink); }
  .attribution__role { font-weight: 400; }
</style>
</head>
<body>
  <article class="quote-post">
    <div class="side-ornament side-ornament--left" role="img" aria-label="Faint decorative leaf pattern"></div>
    <div class="side-ornament side-ornament--right" role="img" aria-label="Faint decorative leaf pattern"></div>

    <div class="brand">
      <span class="brand__dot"></span>
      <span class="brand__name">Lodging Ledger</span>
    </div>

    <div class="portrait">
      <div class="portrait__photo" role="img" aria-label="Portrait photo of Dorian Welk in a navy blazer"></div>
    </div>

    <blockquote class="quote">
      "What we went through is going<br>
      to make the greatest generation of hoteliers<br>
      our industry has ever seen."
    </blockquote>

    <div class="quote__rule"></div>

    <p class="attribution">
      <span class="attribution__name">Dorian Welk</span><br>
      <span class="attribution__role">President, Marrowgate Hotels</span>
    </p>
  </article>
</body>
</html>
```